hi all

Im after a new age looking business card with my company logo on it

must include these details, I would like the PH and Email to be symbols

If the colours used for card could be kept within the colours used in logo that I have supplied that would be great, if another colour is to be used dark grey would be ok. no light bulbs etc thanks

Details below to be incorporated on card

Damian Holloway

Lic E871302

PH 0219647381

E info@brightvaleelectrical.example.nz

Domestic Commercial Industrial Electricians

```html
<!DOCTYPE html>
<html lang="en">
<head>
<meta charset="utf-8">
<title>Brightvale Electrical – Business Card</title>
<link rel="stylesheet" href="https://fonts.googleapis.com/css2?family=Michroma&family=Montserrat:wght@400;500&display=swap">
<style>
  :root {
    --stage: #222222;
    --card-dark: #050505;
    --card-light: #ffffff;
    --brand-blue: #1677c4;
    --ink: #111111;
    --white: #ffffff;
  }
  * { margin: 0; padding: 0; box-sizing: border-box; }
  html, body {
    width: 1200px; height: 900px; overflow: hidden;
    background: var(--stage);
  }
  .canvas {
    position: relative; width: 1200px; height: 900px;
    display: flex; flex-direction: column; align-items: center; justify-content: center; gap: 44px;
  }
  .card {
    position: relative; width: 640px; height: 366px;
    box-shadow: 0 10px 30px rgba(0,0,0,.5);
  }
  /* Front */
  .card--front { background: var(--card-dark); }
  .front-brand {
    position: absolute; left: 0; right: 0; top: 70px;
    display: flex; flex-direction: column; align-items: center; gap: 18px;
  }
  .brand-dot {
    width: 84px; height: 84px; border-radius: 50%;
    background: var(--brand-blue);
  }
  .brand-name {
    font-family: "Michroma", sans-serif; color: var(--brand-blue);
    text-transform: uppercase; text-align: center; line-height: 1.15;
  }
  .card--front .brand-name { font-size: 40px; letter-spacing: 2px; }
  .tagline {
    position: absolute; left: 0; right: 0; bottom: 44px;
    text-align: center; font-family: "Montserrat", sans-serif;
    font-size: 15px; letter-spacing: 1px; color: var(--white); text-transform: uppercase;
  }
  /* Back */
  .card--back { background: var(--card-light); }
  .back-brand {
    position: absolute; left: 40px; top: 32px;
    display: flex; align-items: center; gap: 16px;
  }
  .back-brand .brand-dot { width: 52px; height: 52px; }
  .card--back .brand-name { font-size: 24px; letter-spacing: 1px; text-align: left; }
  .holder-name {
    position: absolute; left: 40px; top: 170px;
    font-family: "Michroma", sans-serif; font-size: 20px; letter-spacing: 1px;
    color: var(--brand-blue); text-transform: uppercase;
  }
  .holder-rule {
    position: absolute; left: 36px; right: 40px; top: 204px;
    height: 2px; background: var(--brand-blue);
  }
  .contact-list {
    position: absolute; left: 40px; top: 228px; list-style: none;
    font-family: "Montserrat", sans-serif; font-size: 18px; color: var(--ink);
  }
  .contact-item { display: flex; align-items: center; gap: 12px; margin-bottom: 8px; }
  .contact-icon { width: 20px; height: 20px; flex: none; }
  .licence {
    position: absolute; right: 40px; bottom: 28px;
    font-family: "Montserrat", sans-serif; font-size: 19px; color: var(--ink);
  }
  .licence-label { color: var(--brand-blue); }
</style>
</head>
<body>
<main class="canvas">
  <section class="card card--front">
    <div class="front-brand">
      <span class="brand-dot"></span>
      <p class="brand-name">Brightvale<br>Electrical</p>
    </div>
    <p class="tagline">Domestic Commercial Industrial Electricians</p>
  </section>

  <section class="card card--back">
    <div class="back-brand">
      <span class="brand-dot"></span>
      <p class="brand-name">Brightvale<br>Electrical</p>
    </div>
    <h1 class="holder-name">Damian Holloway</h1>
    <div class="holder-rule"></div>
    <ul class="contact-list">
      <li class="contact-item">
        <svg class="contact-icon" viewBox="0 0 24 24" fill="none" stroke="var(--brand-blue)" stroke-width="1.8" aria-hidden="true">
          <path d="M6.5 3.5l3 3-2 2.5a12 12 0 0 0 7.5 7.5l2.5-2 3 3-2.5 3C11 20 4 13 3.5 6z" stroke-linejoin="round"/>
        </svg>
        <span>021 964 7381</span>
      </li>
      <li class="contact-item">
        <svg class="contact-icon" viewBox="0 0 24 24" fill="none" stroke="var(--brand-blue)" stroke-width="1.8" aria-hidden="true">
          <rect x="2.5" y="5" width="19" height="14" rx="1"/>
          <path d="M3 6l9 7 9-7" stroke-linejoin="round"/>
        </svg>
        <span>info@brightvaleelectrical.example.nz</span>
      </li>
    </ul>
    <p class="licence"><span class="licence-label">LIC</span> E871302</p>
  </section>
</main>
</body>
</html>
```